Harbourline construction company Business card design

I need a business card design for my company. I have a logo but dont have business cards with our logo..

www.harbourlineconstructco.com.au

The logo is on the website

I need the same details as this design I have attached. we have changed the logo and colours. just like the website

Industry/Entity Type

Building

```html
<!DOCTYPE html>
<html lang="en">
<head>
<meta charset="utf-8">
<title>Harbourline Construction – Business Card</title>
<link href="https://fonts.googleapis.com/css2?family=Roboto:wght@300;400&family=Arimo:wght@400&display=swap" rel="stylesheet">
<style>
  :root {
    --backdrop: #d9d9d9;
    --card: #201c1b;
    --accent: #1f86c8;
    --ink: #f4f4f4;
    --icon: #6e6e6e;
  }
  * { margin: 0; padding: 0; box-sizing: border-box; }
  html, body {
    width: 1200px;
    height: 1000px;
    overflow: hidden;
    background: var(--backdrop);
  }
  .card {
    position: absolute;
    left: 60px;
    top: 146px;
    width: 1080px;
    height: 708px;
    background: var(--card);
    color: var(--ink);
    font-family: "Roboto", sans-serif;
    font-weight: 300;
  }
  .card > * { position: absolute; line-height: 1; white-space: nowrap; }

  .brand {
    left: 90px;
    top: 50px;
    width: 240px;
    text-align: center;
  }
  .brand-square {
    display: block;
    width: 84px;
    height: 84px;
    margin: 0 auto 26px;
    background: var(--accent);
  }
  .brand-name {
    display: block;
    font-weight: 400;
    font-size: 25px;
    letter-spacing: 3px;
    color: var(--accent);
    line-height: 1.25;
  }

  .contact-name {
    right: 70px;
    top: 169px;
    font-size: 45px;
    font-weight: 400;
    text-align: right;
  }
  .contact-role {
    right: 70px;
    top: 226px;
    font-size: 30px;
    text-align: right;
  }

  .divider {
    left: 0;
    top: 301px;
    width: 100%;
    height: 6px;
    background: var(--accent);
  }

  .services { left: 98px; font-size: 36px; }
  .services--first { top: 382px; }
  .services--second { top: 433px; }

  .line { left: 98px; font-size: 35px; }
  .phone-main { top: 520px; }
  .phone-mobile { top: 574px; }
  .email { top: 620px; font-size: 33px; }

  .icon-phone { left: 48px; top: 530px; }
  .icon-mail { left: 52px; top: 632px; }

  .registration {
    left: 1030px;
    top: 430px;
    font-family: "Arimo", sans-serif;
    font-size: 29px;
    writing-mode: vertical-rl;
    transform: rotate(180deg);
  }
</style>
</head>
<body>
  <div class="card">
    <div class="brand">
      <span class="brand-square"></span>
      <span class="brand-name">HARBOURLINE</span>
      <span class="brand-name">CONSTRUCTION</span>
    </div>

    <div class="contact-name">Marek Dalton</div>
    <div class="contact-role">Director</div>

    <div class="divider"></div>

    <div class="services services--first">New Homes - Additions &amp;Renovation</div>
    <div class="services services--second">Domestic &amp; ComercialBuilders</div>

    <svg class="icon-phone" width="26" height="48" viewBox="0 0 26 48" aria-hidden="true">
      <path d="M9 3 L15 3 L16 13 L11 16 Q9 24 11 32 L16 35 L15 45 L9 45 Q2 38 2 24 Q2 10 9 3 Z" fill="var(--icon)"/>
    </svg>
    <div class="line phone-main">08 9412 6630</div>
    <div class="line phone-mobile">0412 558 190</div>

    <svg class="icon-mail" width="28" height="20" viewBox="0 0 28 20" aria-hidden="true">
      <rect x="1" y="1" width="26" height="18" fill="var(--icon)"/>
      <path d="M1 1 L14 12 L27 1" fill="none" stroke="var(--card)" stroke-width="2"/>
    </svg>
    <div class="line email">harbourlineco@mailbox.com</div>

    <div class="registration">Reg. No. 20583</div>
  </div>
</body>
</html>
```